Flyer for Lawnmowing and gardening business

We are a lawn mowing and gardening business needing a flyer designed listing our services and business info.
The flyer should include all business information and contact details as below.

Lawn mowing
Gardening
Green waste removal
Pruning
Weeding
Vegetable Garden Creation

Phone number:0481657240

As well as the logo provided

Target Market(s)

Local people wanting someone to care for their garden.

Industry/Entity Type

Gardener

Font styles to use
Serif

Requirements
Must have
• Business Logo
• All business info and services provided. EG
• Lawn mowing
• Gardening
• Green waste removal
• Pruning
• Weeding
• Vegetable Garden Creation
• Phone number:0481657240
Nice to have
• Earthy tones, clean and simple flyer design

```html
<!DOCTYPE html>
<html lang="en">
<head>
<meta charset="utf-8">
<title>Birchwood Yards – Lawn Mowing &amp; Garden Care</title>
<link rel="stylesheet" href="https://fonts.googleapis.com/css2?family=Cormorant+Garamond:wght@600&family=Amatic+SC:wght@700&family=Lobster&display=swap">
<style>
  :root {
    --paper: #ffffff;
    --ink-brown: #3a2a20;
    --band-slate: #8fa3a8;
    --band-brown: #3b2b21;
    --green-light: #b4d27a;
    --green-mid: #8db356;
    --green-deep: #5f8a34;
    --grass-dark: #4f7a2a;
    --script-green: #b7d98a;
    --white: #ffffff;
  }
  * { margin: 0; padding: 0; box-sizing: border-box; }
  html, body { width: 853px; height: 1200px; overflow: hidden; background: var(--paper); }
  .flyer {
    position: relative;
    width: 853px;
    height: 1200px;
    overflow: hidden;
    background: var(--paper);
  }
  .brand {
    position: absolute;
    top: 0; left: 0; right: 0;
    height: 380px;
    text-align: center;
  }
  .brand-name {
    position: absolute;
    top: 236px; left: 0; right: 0;
    font-family: "Cormorant Garamond", serif;
    font-weight: 600;
    font-size: 74px;
    line-height: 1;
    color: var(--ink-brown);
  }
  .brand-tagline {
    position: absolute;
    top: 322px; left: 0; right: 0;
    font-family: "Cormorant Garamond", serif;
    font-weight: 600;
    font-size: 40px;
    line-height: 1;
    color: var(--ink-brown);
  }
  .rule-slate {
    position: absolute;
    top: 382px; left: 0; right: 0;
    height: 18px;
    background: var(--band-slate);
  }
  .band-brown {
    position: absolute;
    top: 410px; left: 0; right: 0;
    height: 150px;
    background: var(--band-brown);
  }
  .field {
    position: absolute;
    top: 560px; left: 0; right: 0; bottom: 0;
    background: linear-gradient(180deg, var(--green-light) 0%, var(--green-mid) 55%, var(--green-deep) 100%);
  }
  .grass {
    position: absolute;
    left: 0; right: 0; bottom: 0;
    height: 130px;
    background: linear-gradient(180deg, rgba(79,122,42,0) 0%, var(--grass-dark) 100%);
  }
  .services-frame {
    position: absolute;
    top: 472px; left: 85px;
    width: 683px; height: 578px;
    border: 6px dotted var(--white);
  }
  .services-title {
    position: absolute;
    top: 472px; left: 0; right: 0;
    text-align: center;
    font-family: "Lobster", cursive;
    font-size: 62px;
    line-height: 1;
    color: var(--script-green);
    text-shadow: 2px 2px 0 #1d140f;
  }
  .services-list {
    position: absolute;
    top: 566px; left: 0; right: 0;
    list-style: none;
    text-align: center;
    font-family: "Amatic SC", sans-serif;
    font-weight: 700;
    font-size: 70px;
    line-height: 62px;
    color: var(--white);
    letter-spacing: 2px;
    text-shadow: 1px 2px 2px rgba(40,50,20,0.35);
  }
  .phone {
    position: absolute;
    top: 948px; left: 0; right: 0;
    text-align: center;
    font-family: "Lobster", cursive;
    font-size: 74px;
    line-height: 1;
    color: var(--white);
    letter-spacing: 2px;
    -webkit-text-stroke: 2px #2f4a1a;
    text-shadow: 3px 3px 0 #2f4a1a;
  }
  .phone-rule {
    position: absolute;
    top: 1064px; left: 170px;
    width: 513px; height: 5px;
    background: var(--ink-brown);
  }
</style>
</head>
<body>
  <main class="flyer">
    <header class="brand">
      <h1 class="brand-name">Birchwood Yards</h1>
      <p class="brand-tagline">Lawn Mowing &amp; Garden Care</p>
    </header>
    <div class="rule-slate"></div>
    <div class="band-brown"></div>
    <div class="field">
      <div class="grass" role="img" aria-label="Silhouette of grass blades along the bottom edge"></div>
    </div>
    <div class="services-frame"></div>
    <h2 class="services-title">Services Offered</h2>
    <ul class="services-list">
      <li>Lawn Mowing</li>
      <li>Gardening</li>
      <li>Green Waste Removal</li>
      <li>Pruning</li>
      <li>Weeding</li>
      <li>Vegetable Garden Creation</li>
    </ul>
    <p class="phone">0481657240</p>
    <div class="phone-rule"></div>
  </main>
</body>
</html>
```